Tequila Startup Company Booklet Design

Need a 16 or so page booklet for a spirits company (like tequila) artfully designed. Need a killer design and beautifully and thoughtfully laid out in a compelling manner. Need talented and creative designer to craft an eye catching booklet.
Updates

Low designer entries

Target Market(s)

Investors and tequila drinkers

Industry/Entity Type

Alcohol spirits distillery

Colors

Designer to choose colors to be used in the design.

Requirements
Must have
• Beautiful graphics and photos relevant to agave fields
Nice to have
• Want to emphasize the blue agave fields and the distillery process

```html
<!DOCTYPE html>
<html lang="en">
<head>
<meta charset="utf-8">
<title>Alvera Tequila — Investor Booklet</title>
<link rel="stylesheet" href="https://fonts.googleapis.com/css2?family=Outfit:wght@400;500;600;700&family=Mulish:wght@400;600;700&display=swap">
<style>
:root{
  --teal:#1895a9;
  --yellow:#dccf2c;
  --ink:#111;
  --body:#2a2a2a;
  --white:#fff;
  --backdrop:#f3f3f3;
}
*{margin:0;padding:0;box-sizing:border-box}
html,body{width:875px;height:1200px;overflow:hidden;background:var(--backdrop)}
body{position:relative;font-family:"Mulish",sans-serif;color:var(--body)}
.page{position:absolute;width:379px;height:536px;background:var(--white);overflow:hidden;box-shadow:0 1px 3px rgba(0,0,0,.12)}
.p1{left:48px;top:45px}.p2{left:458px;top:45px}.p3{left:48px;top:613px}.p4{left:458px;top:613px}
.abs{position:absolute}
.heading{font-family:"Outfit",sans-serif;color:var(--ink);font-weight:500}
/* cover */
.cover-brand{left:0;right:0;top:10px;display:flex;justify-content:center;align-items:center;gap:6px}
.brand-dot{width:32px;height:32px;border-radius:50%;background:var(--teal)}
.brand-name{font-family:"Outfit",sans-serif;font-weight:700;font-size:19px;color:var(--teal);letter-spacing:.2px}
.cover-photo{left:0;top:48px;width:379px;height:300px;background:linear-gradient(180deg,#4b5a7a 0%,#d87a3a 22%,#6b6a3a 40%,#b9b84a 52%,#3e6f86 70%,#2f5a6c 100%)}
.cover-shape{left:0;top:0}
.cover-kicker{left:0;width:348px;top:357px;text-align:center;font-family:"Outfit",sans-serif;font-size:16px;color:var(--white)}
.cover-rule{left:159px;top:385px;width:46px;height:1.5px;background:var(--white)}
.cover-title{left:0;width:348px;top:395px;text-align:center;font-family:"Outfit",sans-serif;font-weight:600;font-size:31px;line-height:34px;color:var(--white)}
/* section header */
.band{left:0;top:13px;width:379px;height:25px;background:var(--teal)}
.band-dot{top:7px;width:38px;height:38px;border-radius:50%;background:var(--teal);border:3px solid var(--white)}
.band-title{left:88px;top:13px;line-height:25px;font-family:"Outfit",sans-serif;font-weight:700;font-size:18px;color:var(--white);letter-spacing:.3px}
.page-title{left:19px;top:57px;font-size:16px}
.accent{height:2px;display:flex;gap:3px}
.accent i{display:block;height:2px;border-radius:1px}
.accent .t{width:34px;background:var(--teal)}.accent .y{width:10px;background:var(--yellow)}
/* footer */
.footer{left:0;bottom:0;width:379px;height:16px;background:var(--teal);color:var(--white);font-size:5.6px;line-height:16px;padding-left:19px}
.page-num{position:absolute;right:19px;top:2px;width:12px;height:12px;border-radius:50%;background:var(--white);color:var(--teal);font-size:6px;line-height:12px;text-align:center;font-weight:700}
/* welcome */
.greeting{left:19px;top:96px;font-family:"Outfit",sans-serif;font-size:13px;color:var(--teal)}
.letter{font-size:7.2px;line-height:12.2px;color:var(--body)}
.letter p{margin-bottom:12.2px}
.letter-narrow{left:19px;top:119px;width:220px}
.letter-wide{left:19px;top:256px;width:332px}
.portrait{left:264px;top:95px;width:96px;height:98px;background:linear-gradient(135deg,#c9d2cf,#7f8d8a 60%,#283140)}
.signoff{left:19px;top:430px;font-family:"Outfit",sans-serif;font-weight:600;font-size:9px;color:var(--ink)}
.signature{left:22px;top:454px;width:62px;height:16px;background:linear-gradient(90deg,rgba(40,40,40,.18),rgba(40,40,40,.05))}
/* vision */
.tick-list{left:19px;top:94px;width:290px;list-style:none}
.tick-list li{position:relative;padding-left:10px;font-size:6.5px;line-height:10px;margin-bottom:11px}
.tick{position:absolute;left:0;top:2px}
.vm-band{left:0;top:191px;width:379px;height:86px;background:var(--yellow)}
.vm-mission{left:182px;top:191px;width:197px;height:86px;background:var(--teal);border-radius:46px 0 0 46px;border-left:2px solid var(--white)}
.vm-title{font-family:"Outfit",sans-serif;font-size:13px;color:var(--white);font-weight:500}
.vm-accent{height:2px;display:flex;gap:3px;margin:4px 0 6px}
.vm-accent i{display:block;height:2px;border-radius:1px}
.vm-text{position:relative;padding-left:8px;font-size:5.8px;line-height:9px;color:var(--white);width:150px}
.vm-text::before{content:"";position:absolute;left:0;top:2.5px;width:3.5px;height:3.5px;border-radius:50%;background:var(--white)}
.distillery{left:0;top:278px;width:379px;height:242px;background:linear-gradient(180deg,#3a2c22 0%,#6b4a32 35%,#8a6a4a 60%,#a2794f 100%)}
/* story */
.col-head{font-family:"Outfit",sans-serif;font-weight:500;font-size:9.5px;color:var(--ink);display:flex;align-items:center;gap:4px}
.arrow-list{list-style:none;margin-top:5px;padding-left:8px}
.arrow-list li{position:relative;padding-left:7px;font-size:6.3px;line-height:13.8px;color:var(--ink)}
.arrow-list li::before{content:"";position:absolute;left:0;top:4.5px;border-left:3px solid var(--teal);border-top:2.5px solid transparent;border-bottom:2.5px solid transparent}
.story-head{font-family:"Outfit",sans-serif;font-weight:500;font-size:12px;color:var(--ink)}
.story-text{font-size:5.3px;line-height:8.7px;color:var(--body);width:168px;margin-top:4px}
.photo{border-radius:3px}
</style>
</head>
<body>

<!-- Cover -->
<section class="page p1">
  <div class="abs cover-photo" role="img" aria-label="Sunset over a volcano above rows of blue agave and a hacienda"></div>
  <svg class="abs cover-shape" width="379" height="536" viewBox="0 0 379 536" aria-hidden="true">
    <path d="M290 340 C292 305 318 290 379 288 L379 536 L290 536 Z" fill="#dccf2c"/>
    <path d="M0 290 L300 326 C332 330 348 352 348 384 L348 536 L0 536 Z" fill="#1895a9"/>
  </svg>
  <div class="abs cover-brand"><span class="brand-dot"></span><span class="brand-name">ALVERA TEQUILA</span></div>
  <p class="abs cover-kicker">The Future of Premium Tequila</p>
  <div class="abs cover-rule"></div>
  <h1 class="abs cover-title">Rooted in Heritage.<br>Distilled for the<br>Future.</h1>
</section>

<!-- Welcome -->
<section class="page p2">
  <div class="abs band"></div>
  <div class="abs band-dot" style="left:36px"></div>
  <h2 class="abs band-title">WELCOME</h2>
  <h3 class="abs heading page-title">A Message to Our Investors</h3>
  <div class="abs accent" style="left:19px;top:82px"><i class="t"></i><i class="y"></i></div>
  <p class="abs greeting">Dear Future Partners,</p>
  <div class="abs letter letter-narrow">
    <p>It is with great pride and deep excitement that I welcome you to the story of Alvera Tequila — a brand born from tradition, nurtured by craft, and driven by vision.</p>
    <p>Our journey began in the sun-soaked fields of Jalisco, where generations have grown and harvested the legendary blue agave. From the very start, we were determined to create something truly exceptional — not just another tequila, but an elevated experience that honors the heart of Mexico while setting a new standard in luxury spirits.</p>
  </div>
  <div class="abs portrait" role="img" aria-label="Portrait of the company founder"></div>
  <div class="abs letter letter-wide">
    <p>With our roots firmly grounded in tradition and our eyes on innovation, Alvera Tequila is more than a product — it’s a movement. A refined spirit for a discerning audience. A timeless story ready to be told.</p>
    <p>As we prepare to launch, I invite you to be part of something extraordinary. With your investment, we're not just building a brand — we're cultivating legacy.</p>
    <p>With our roots firmly grounded in tradition and our eyes on innovation, Alvera Tequila is more than a product — it’s a movement. A refined spirit for a discerning audience. A timeless story ready to be told.</p>
    <p>As we prepare to launch, I invite you to be part of something extraordinary. With your investment, we're not just building a brand — we're cultivating legacy.</p>
  </div>
  <p class="abs signoff">Warm Regards</p>
  <div class="abs signature" role="img" aria-label="Handwritten signature"></div>
  <footer class="abs footer">Copyrights@2025.Company Name.All Rights Reserved<span class="page-num">2</span></footer>
</section>

<!-- Vision & Mission -->
<section class="page p3">
  <div class="abs band"></div>
  <div class="abs band-dot" style="left:36px"></div>
  <h2 class="abs band-title">VISION &amp; MISSION</h2>
  <h3 class="abs heading page-title">Our vision</h3>
  <div class="abs accent" style="left:19px;top:82px"><i class="t"></i><i class="y"></i></div>
  <ul class="abs tick-list">
    <li><svg class="tick" width="6" height="6" viewBox="0 0 6 6"><circle cx="3" cy="3" r="3" fill="#1895a9"/><path d="M1.6 3.1 L2.6 4 L4.4 2" stroke="#fff" stroke-width=".8" fill="none"/></svg>Lorem ipsum dolor sit amet, consectetur adipiscing elit, sed do eiusmod tempor incididunt ut labore et dolore magna aliqua.</li>
    <li><svg class="tick" width="6" height="6" viewBox="0 0 6 6"><circle cx="3" cy="3" r="3" fill="#1895a9"/><path d="M1.6 3.1 L2.6 4 L4.4 2" stroke="#fff" stroke-width=".8" fill="none"/></svg>Ut enim ad minim veniam, quis nostrud exercitation ullamco laboris nisi ut aliquip ex ea commodo consequat.</li>
    <li><svg class="tick" width="6" height="6" viewBox="0 0 6 6"><circle cx="3" cy="3" r="3" fill="#1895a9"/><path d="M1.6 3.1 L2.6 4 L4.4 2" stroke="#fff" stroke-width=".8" fill="none"/></svg>Duis aute irure dolor in reprehenderit in voluptate velit esse cillum dolore eu fugiat nulla pariatur.</li>
  </ul>
  <div class="abs vm-band"></div>
  <div class="abs vm-mission"></div>
  <div class="abs" style="left:19px;top:205px">
    <p class="vm-title">Our vision</p>
    <div class="vm-accent"><i style="width:28px;background:var(--teal)"></i><i style="width:8px;background:var(--white)"></i></div>
    <p class="vm-text">Excepteur sint occaecat cupidatat non proident, sunt in culpa qui officia deserunt mollit anim id est laborum.</p>
  </div>
  <div class="abs" style="left:214px;top:205px">
    <p class="vm-title">Our Mission</p>
    <div class="vm-accent"><i style="width:28px;background:var(--yellow)"></i><i style="width:8px;background:var(--white)"></i></div>
    <p class="vm-text">Excepteur sint occaecat cupidatat non proident, sunt in culpa qui officia deserunt mollit anim id est laborum.</p>
  </div>
  <div class="abs distillery" role="img" aria-label="Distillery tasting hall with oak barrels and brick columns"></div>
  <footer class="abs footer">Copyrights@2025.Company Name.All Rights Reserved<span class="page-num">3</span></footer>
</section>

<!-- The Story -->
<section class="page p4">
  <div class="abs band"></div>
  <div class="abs band-dot" style="left:36px"></div>
  <h2 class="abs band-title">THE STORY</h2>
  <h3 class="abs heading page-title">Born From Tradition</h3>
  <div class="abs accent" style="left:19px;top:82px"><i class="t"></i><i class="y"></i></div>
  <div class="abs" style="left:20px;top:96px">
    <p class="col-head"><svg width="8" height="8" viewBox="0 0 6 6"><circle cx="3" cy="3" r="3" fill="#1895a9"/><path d="M1.6 3.1 L2.6 4 L4.4 2" stroke="#fff" stroke-width=".8" fill="none"/></svg>Lorem ipsum dolor sit amet</p>
    <ul class="arrow-list"><li>Sed ut perspiciatis unde omnis iste</li><li>Natus error sit voluptatem accusantium</li><li>Doloremque laudantium, totam rem</li><li>Aperiam, eaque ipsa</li><li>Quae ab illo inventore veritatis</li></ul>
  </div>
  <div class="abs" style="left:202px;top:96px">
    <p class="col-head"><svg width="8" height="8" viewBox="0 0 6 6"><circle cx="3" cy="3" r="3" fill="#dccf2c"/><path d="M1.6 3.1 L2.6 4 L4.4 2" stroke="#fff" stroke-width=".8" fill="none"/></svg>Lorem ipsum dolor sit amet</p>
    <ul class="arrow-list"><li>Sed ut perspiciatis unde omnis iste</li><li>Natus error sit voluptatem accusantium</li><li>Doloremque laudantium, totam rem</li><li>Aperiam, eaque ipsa</li><li>Quae ab illo inventore veritatis</li></ul>
  </div>

  <div class="abs" style="left:20px;top:198px">
    <h4 class="story-head">Brand Origin</h4>
    <p class="story-text">Lorem ipsum dolor sit amet, consectetur adipiscing elit, sed do eiusmod tempor incididunt ut labore et dolore magna aliqua. Ut enim ad minim veniam, quis nostrud exercitation ullamco laboris nisi ut aliquip ex ea commodo consequat. Duis aute irure dolor in reprehenderit in voluptate velit esse cillum dolore eu fugiat nulla pariatur. Excepteur sint occaecat cupidatat non proident, sunt in culpa qui officia deserunt mollit anim id est laborum.</p>
  </div>
  <div class="abs photo" style="left:206px;top:199px;width:153px;height:86px;background:linear-gradient(160deg,#c9b35a,#5d7a2c 45%,#1f3a14)" role="img" aria-label="Rolling green hills of farmland at golden hour"></div>

  <div class="abs photo" style="left:20px;top:305px;width:153px;height:87px;background:linear-gradient(180deg,#8fb4d6 0%,#b8a88a 45%,#7d6a52 70%,#a86e4c 100%)" role="img" aria-label="Travellers standing before ancient temple ruins"></div>
  <div class="abs" style="left:190px;top:305px">
    <h4 class="story-head">Cultural Heritage</h4>
    <p class="story-text">Lorem ipsum dolor sit amet, consectetur adipiscing elit, sed do eiusmod tempor incididunt ut labore et dolore magna aliqua. Ut enim ad minim veniam, quis nostrud exercitation ullamco laboris nisi ut aliquip ex ea commodo consequat. Duis aute irure dolor in reprehenderit in voluptate velit esse cillum dolore eu fugiat nulla pariatur. Excepteur sint occaecat cupidatat non proident, sunt in culpa qui officia deserunt mollit anim id est laborum.</p>
  </div>

  <div class="abs" style="left:18px;top:410px">
    <h4 class="story-head">Inspiration behind the venture</h4>
    <p class="story-text">Lorem ipsum dolor sit amet, consectetur adipiscing elit, sed do eiusmod tempor incididunt ut labore et dolore magna aliqua. Ut enim ad minim veniam, quis nostrud exercitation ullamco laboris nisi ut aliquip ex ea commodo consequat. Duis aute irure dolor in reprehenderit in voluptate velit esse cillum dolore eu fugiat nulla pariatur. Excepteur sint occaecat cupidatat non proident, sunt in culpa qui officia deserunt mollit anim id est laborum.</p>
  </div>
  <div class="abs photo" style="left:206px;top:411px;width:153px;height:87px;background:linear-gradient(170deg,#e0a040,#8a6a2a 35%,#3d4a1e 70%,#1e2a12)" role="img" aria-label="Winding road through hills at sunset"></div>
  <footer class="abs footer">Copyrights@2025.Company Name.All Rights Reserved<span class="page-num">4</span></footer>
</section>

</body>
</html>
```